Ferncrest Dental, LLC business card project

Business card to be designed with current logo.
Dental office- please keep design of card that looks clean and professional.
Please include the following info:
Ferncrest Dental, LLC
Dr. Lorna Pettigrew
2871 Marlowe Street
Fernvale, OH 44093
555-555-0193
ferncrestdental.office@examplemail.test
Hello everyone-
Reason: Just got back from overseas- will look at all designs and provide feedback. Thank you!
Reason: Polling my friends for the final selection-
thank you to all those that participated- so many talented designers!

```html
<!DOCTYPE html>
<html lang="en">
<head>
<meta charset="utf-8">
<title>Ferncrest Dental – Business Card</title>
<link rel="stylesheet" href="https://fonts.googleapis.com/css2?family=Source+Sans+3:wght@400;600&display=swap">
<style>
  :root {
    --backdrop: #8d8d8d;
    --card: #ffffff;
    --lime: #a8d02a;
    --leaf: #5ea534;
    --name-green: #5b9f30;
    --text-lime: #94c11f;
    --tooth-tint: #e4efdb;
    --card-shadow: rgba(0, 0, 0, 0.28);
  }
  * { box-sizing: border-box; margin: 0; padding: 0; }
  html, body {
    width: 1200px;
    height: 964px;
    overflow: hidden;
    background: var(--backdrop);
    font-family: "Source Sans 3", "Myriad Pro", sans-serif;
  }
  .canvas {
    position: relative;
    width: 1200px;
    height: 964px;
  }
  .card {
    position: absolute;
    left: 300px;
    width: 600px;
    height: 343px;
    background: var(--card);
    box-shadow: 0 6px 18px var(--card-shadow);
    overflow: hidden;
  }
  .card--brand { top: 105px; }
  .card--contact { top: 512px; }

  /* Brand side */
  .stripe {
    position: absolute;
    left: 0;
    width: 100%;
    height: 9px;
  }
  .stripe--top { top: 44px; background: var(--lime); }
  .stripe--bottom { top: 272px; background: var(--leaf); }
  .brand-lockup {
    position: absolute;
    top: 0;
    left: 0;
    width: 100%;
    height: 343px;
    display: flex;
    align-items: center;
    justify-content: center;
    gap: 12px;
  }
  .brand-lockup__dot {
    width: 16px;
    height: 16px;
    border-radius: 50%;
    background: var(--lime);
  }
  .brand-lockup__name {
    font-size: 38px;
    font-weight: 400;
    color: var(--lime);
    letter-spacing: 0.2px;
  }

  /* Contact side */
  .contact__name {
    position: absolute;
    top: 40px;
    left: 44px;
    font-size: 34px;
    font-weight: 600;
    color: var(--name-green);
    line-height: 1.2;
  }
  .contact__details {
    position: absolute;
    top: 92px;
    left: 60px;
    list-style: disc;
    color: var(--text-lime);
    font-size: 15px;
    line-height: 20px;
  }
  .contact__details li { padding-left: 2px; }
  .tooth-emblem {
    position: absolute;
    top: 62px;
    left: 420px;
    width: 140px;
    height: 168px;
    border-radius: 40px;
    background: linear-gradient(to bottom, var(--tooth-tint), rgba(228, 239, 219, 0.4));
    opacity: 0.75;
  }
  .contact__band {
    position: absolute;
    left: 0;
    top: 196px;
    width: 100%;
    height: 122px;
    background: linear-gradient(to bottom, var(--lime) 0%, var(--leaf) 100%);
  }
</style>
</head>
<body>
<main class="canvas">
  <section class="card card--brand" aria-label="Business card front">
    <div class="stripe stripe--top"></div>
    <div class="brand-lockup">
      <span class="brand-lockup__dot"></span>
      <span class="brand-lockup__name">FerncrestDental</span>
    </div>
    <div class="stripe stripe--bottom"></div>
  </section>

  <section class="card card--contact" aria-label="Business card back">
    <div class="contact__band"></div>
    <div class="tooth-emblem" role="img" aria-label="Faint practice emblem decoration"></div>
    <h1 class="contact__name">Dr. Lorna Pettigrew</h1>
    <ul class="contact__details">
      <li>2871 Marlowe Street</li>
      <li>Fernvale, OH 44093</li>
      <li>555-555-0193</li>
      <li>ferncrestdental.office@examplemail.test</li>
    </ul>
  </section>
</main>
</body>
</html>
```